New solo practice law firm is looking for an elegant, professional, and interactive web design

I need a web design and developer for a new small law firm in Sacramento, California called Dorian Kessel Law, A Professional Corporation. I am a trial lawyer who represents average people facing difficult litigation disputes, including criminal defense as a former prosecutor and civil litigation as a civil litigator. Criminal defense includes domestic violence, battery, assault, drug possession, theft, DUI, etc. Civil litigation includes business disputes, property disputes, employment disputes, family law disputes, and immigration issues. I would like to see web designs that incorporate my logo and use the logo's navy blue and gold colors. I have uploaded the files of my logo to this brief. Please only use the navy blue and gold version. Overall, I want the design to look firm, professional, and elegant.

I plan on having the following pages on my website: (1) Home, (2) Dorian Kessel, (3) Practice Areas, (4) Insights, (5) Contact. I've hand drawn a preliminary sketch concept of what I envision the home page's layout to look like (attached with a text version). I would like your design to keep a similar layout for the homepage and incorporate my logo's colors within it but I am open to creative layout alternatives/ideas. I would like the other pages to have a similar look and feel as the home page. Some of the areas currently in my sketch do not have the full text. You can insert other text for now and I will provide the winner the full text.

In terms of the pictures on the website, I enjoy images of courthouses, columns (example attached but I cannot use this one), and, if possible, images from Sacramento, CA in my background (headshot attached). A plus would be live images that move and also sections of the webpage moving in the viewers view as they scroll down on the page. Also, it would be great to have my logo act as the tab for the website. I can provide other versions of the logo if needed.

I look forward to seeing your Wordpress designs!

People needing legal representation.

Law

Coded - Design and coding required

5+ page

Serif

• Incorporate my logo and my logo's colors.
• Live pictures and images appearing as viewers scroll on page.

```html
<!DOCTYPE html>
<html lang="en">
<head>
<meta charset="utf-8">
<title>Dorian Kessel Law</title>
<link href="https://fonts.googleapis.com/css2?family=Mulish:wght@400;500;600&family=Encode+Sans+Condensed:wght@400;500&display=swap" rel="stylesheet">
<style>
:root{
  --navy:#14213d;
  --navy-deep:#111c33;
  --gold:#a38a55;
  --gold-light:#c9ad6e;
  --text:#222;
  --muted:#555;
  --white:#fff;
}
*{box-sizing:border-box;margin:0;padding:0}
html,body{width:1200px;height:3250px;overflow:hidden}
body{position:relative;font-family:'Mulish',sans-serif;color:var(--text);background:var(--white)}
.abs{position:absolute}
svg.icon{width:18px;height:18px;fill:none;stroke:currentColor;stroke-width:1.4;vertical-align:middle}

/* header */
.site-header{left:0;top:0;width:1200px;height:150px;background:var(--navy)}
.topbar{left:540px;top:0;width:660px;height:36px;background:var(--gold);clip-path:polygon(18px 0,100% 0,100% 100%,36px 100%);color:var(--white);font-size:13px;display:flex;align-items:center;padding-left:60px;gap:6px}
.topbar .lang{margin-left:18px;display:flex;align-items:center;gap:5px}
.topbar .lang i{display:inline-block;width:22px;height:22px;border-radius:50%;background:linear-gradient(#b22 0 50%,#fff 50% 60%,#b22 60%);}
.brand{left:165px;top:42px;display:flex;align-items:center;gap:10px;color:var(--gold-light);font-size:18px;font-weight:500;letter-spacing:2px;text-transform:uppercase}
.brand .mark{width:18px;height:18px;border:2px solid var(--gold-light)}
.header-phone{right:163px;top:62px;color:var(--gold-light);font-size:17px;display:flex;align-items:center;gap:10px}
.main-nav{right:163px;top:104px;display:flex;gap:32px;font-size:14px;color:var(--white)}
.main-nav a{color:inherit;text-decoration:none}
.main-nav a.active{color:var(--gold-light)}

/* hero */
.hero{left:0;top:150px;width:1200px;height:600px;background:linear-gradient(180deg,#2b4272 0%,#3a5283 45%,#4e6390 75%,#2d416b 100%)}
.hero-curve{left:0;top:150px;width:1200px;height:600px}
.hero h1{left:0;top:322px;width:1200px;text-align:center;color:var(--white);font-weight:500;font-size:55px}
.hero p{left:0;top:398px;width:1200px;text-align:center;color:var(--white);font-family:'Encode Sans Condensed',sans-serif;font-size:22px;line-height:31px}
.btn{display:flex;align-items:center;justify-content:center;gap:12px;font-size:17px;color:var(--white)}
.btn-gold{background:var(--gold)}
.btn-navy{background:var(--navy)}
.hero .btn,.practice .btn{}
.cta-hero{left:414px;top:470px;width:372px;height:48px}

/* practice */
.section-title{left:0;width:1200px;text-align:center;color:var(--gold);font-size:34px;font-weight:500}
.rule{height:2px;background:var(--navy);width:76px}
.section-lead{left:0;width:1200px;text-align:center;font-size:16px;line-height:26px;color:var(--text)}
.card{top:985px;width:203px;height:320px;background:var(--white);box-shadow:0 4px 14px rgba(0,0,0,.09);padding:0 10px}
.card .photo{width:182px;height:168px}
.card h3{color:var(--gold);font-weight:500;font-size:16px;margin:15px 0 10px}
.card p{font-size:13px;line-height:20px;color:var(--text)}
.card a{display:block;margin-top:11px;font-size:13px;color:var(--gold);text-decoration:underline}
.cta-practice{left:414px;top:1337px;width:372px;height:48px}

/* about */
.about{left:0;top:1511px;width:1200px;height:637px;background:linear-gradient(180deg,#2a3c62 0%,#24365a 50%,#1c2c49 100%)}
.portrait{left:712px;top:1445px;width:360px;height:703px;background:linear-gradient(180deg,#3a2f2a 0%,#23242c 40%,#141820 100%);border-radius:160px 160px 0 0}
.eyebrow{left:162px;top:1651px;color:var(--white);font-size:19px;letter-spacing:3px}
.about h2{left:162px;top:1676px;color:var(--white);font-size:34px;font-weight:500}
.about-rule{left:162px;top:1722px;background:var(--white)}
.about-copy{left:162px;top:1743px;width:530px;color:var(--white);font-size:13.5px;line-height:23px}
.about-copy p+p{margin-top:11px}
.about-btn{left:162px;top:1956px;width:220px;height:47px}

/* contact */
.contact-band{left:0;top:2742px;width:1200px;height:508px;background:var(--navy)}
.contact-card{left:162px;top:2359px;width:877px;height:456px;display:flex;box-shadow:0 4px 18px rgba(0,0,0,.08)}
.form-panel{width:438px;background:var(--gold);padding:55px 44px 0 35px;color:var(--navy)}
.form-panel h3{font-size:22px;font-weight:500}
.form-panel .rule{margin:18px 0 22px;width:52px}
.field{display:flex;align-items:center;gap:18px;height:52px;border-bottom:1px solid var(--navy);font-size:12px;padding-left:0}
.field.tall{height:82px;align-items:flex-start;padding-top:16px}
.submit{margin-top:33px;width:140px;height:41px;background:var(--navy);color:var(--white);font-size:16px;display:flex;align-items:center;justify-content:center}
.info-panel{flex:1;background:var(--white);padding:115px 20px 0 19px}
.info-panel h3{font-size:32px;font-weight:500;line-height:45px;color:var(--navy)}
.info-panel p{margin-top:12px;font-size:13px;line-height:24px}

/* footer */
.footer-brand{left:195px;top:2990px;display:flex;align-items:center;gap:10px;color:var(--gold-light);font-size:17px;letter-spacing:2px;text-transform:uppercase}
.footer-brand .mark{width:18px;height:18px;border:2px solid var(--gold-light)}
.social{left:246px;top:3046px;display:flex;gap:5px}
.social span{width:30px;height:30px;border:1px solid var(--gold-light)}
.f-title{color:var(--gold-light);font-size:19px;font-weight:500}
.f-rule{background:var(--gold-light);width:52px}
.f-item{display:flex;gap:18px;color:var(--gold-light);font-size:13px;line-height:22px}
.f-item .circ{width:38px;height:38px;border:1px solid var(--gold-light);border-radius:50%;display:flex;align-items:center;justify-content:center;flex:none}
.quick{left:887px;top:2940px;list-style:none;color:var(--gold-light);font-size:13px;line-height:24.5px}
.quick li::before{content:"›";margin-right:7px}
.disclaimer{left:180px;top:3123px;width:840px;text-align:center;color:var(--gold-light);font-size:11.5px;line-height:18px}
.footer-line{left:162px;top:3190px;width:877px;height:1px;background:rgba(201,173,110,.25)}
.copyright{left:0;top:3205px;width:1200px;text-align:center;color:var(--gold-light);font-size:13px}
</style>
</head>
<body>

<header class="site-header abs"></header>
<div class="topbar abs">
  <svg class="icon" viewBox="0 0 20 20"><path d="M10 18s6-6 6-10a6 6 0 0 0-12 0c0 4 6 10 6 10z"/><circle cx="10" cy="8" r="2"/></svg>
  2870 Larkspur Avenue, Suite #304, Elk Grove, CA 95758
  <span class="lang"><i></i>EN ⌄</span>
</div>
<div class="brand abs"><span class="mark"></span>Dorian Kessel Law</div>
<div class="header-phone abs">
  <svg class="icon" viewBox="0 0 20 20" style="width:24px;height:24px"><path d="M4 3l3 0 2 4-2 1.5a10 10 0 0 0 4.5 4.5L13 11l4 2v3a2 2 0 0 1-2 2A13 13 0 0 1 2 5a2 2 0 0 1 2-2z"/></svg>
  Free Consultation &nbsp; (916) 555-0148
</div>
<nav class="main-nav abs">
  <a class="active" href="#">Home</a><a href="#">Dorian Kessel</a><a href="#">Pracitce Areas</a><a href="#">Insights</a><a href="#">Contact</a>
</nav>

<section class="hero-wrap">
  <div class="hero abs" role="img" aria-label="Courthouse facade with classical columns under a blue overlay"></div>
  <svg class="hero-curve abs" viewBox="0 0 1200 600" preserveAspectRatio="none">
    <polygon points="0,530 600,585 1200,530 1200,540 600,595 0,540" fill="#a38a55"/>
    <polygon points="0,540 600,595 1200,540 1200,600 0,600" fill="#fff"/>
  </svg>
  <div class="hero"><h1 class="abs" style="top:322px">Dorian Kessel Law</h1></div>
  <p class="abs" style="left:0;top:398px;width:1200px;text-align:center;color:#fff;font-family:'Encode Sans Condensed',sans-serif;font-size:22px;line-height:31px">A Trial Lawyer Who Represents Average People Facing Difficult Litigation Disputes,<br>Including Criminal Defense As A Former Prosecutor And Civil Litigation As A Civil Litigator</p>
  <div class="btn btn-gold cta-hero abs">
    <svg class="icon" viewBox="0 0 20 20" style="width:24px;height:24px"><path d="M4 3l3 0 2 4-2 1.5a10 10 0 0 0 4.5 4.5L13 11l4 2v3a2 2 0 0 1-2 2A13 13 0 0 1 2 5a2 2 0 0 1 2-2z"/></svg>
    Free Consultation &nbsp; (916) 555-0148
  </div>
</section>

<section class="practice">
  <h2 class="section-title abs" style="top:815px">Criminal And Civil Trial Lawyers</h2>
  <div class="rule abs" style="left:562px;top:865px"></div>
  <p class="section-lead abs" style="top:877px">Dorian Kessel Law is a law firm serving the Sacramento, Yolo, San Joaquin, Solano and Stanislaus Counties.<br>We represent clients in a wide array of criminal, civil, family law, and immigration cases.</p>

  <article class="card abs" style="left:162px">
    <div class="photo" role="img" aria-label="Handcuffed hands resting on a table" style="background:linear-gradient(160deg,#6b3a22,#b7653a 60%,#3b1d12)"></div>
    <h3>Criminal Defense</h3>
    <p>Lorem ipsum dolor sit amet, consectetuer adipiscing elit, sed diam nonummy...</p>
    <a href="#">Read More</a>
  </article>
  <article class="card abs" style="left:387px">
    <div class="photo" role="img" aria-label="Judge's gavel on a desk with people in the background" style="background:linear-gradient(160deg,#e4e6ea,#c7cbd2 55%,#8a7a66)"></div>
    <h3>Civil Litigation</h3>
    <p>Lorem ipsum dolor sit amet, consectetuer adipiscing elit, sed diam nonummy...</p>
    <a href="#">Read More</a>
  </article>
  <article class="card abs" style="left:612px">
    <div class="photo" role="img" aria-label="Gavel beside immigration law books" style="background:linear-gradient(160deg,#5a3d2b,#d8d2c8 50%,#efece6)"></div>
    <h3>Immigration</h3>
    <p>Lorem ipsum dolor sit amet, consectetuer adipiscing elit, sed diam nonummy...</p>
    <a href="#">Read More</a>
  </article>
  <article class="card abs" style="left:836px">
    <div class="photo" role="img" aria-label="Scales of justice and wooden family figures" style="background:linear-gradient(160deg,#c7c9b8,#8d8a6d 55%,#2f4a3c)"></div>
    <h3>Family Law</h3>
    <p>Lorem ipsum dolor sit amet, consectetuer adipiscing elit, sed diam nonummy...</p>
    <a href="#">Read More</a>
  </article>

  <div class="btn btn-navy cta-practice abs">
    <svg class="icon" viewBox="0 0 20 20" style="width:24px;height:24px;color:#c9ad6e"><path d="M4 3l3 0 2 4-2 1.5a10 10 0 0 0 4.5 4.5L13 11l4 2v3a2 2 0 0 1-2 2A13 13 0 0 1 2 5a2 2 0 0 1 2-2z"/></svg>
    <span style="color:#c9ad6e">Free Consultation &nbsp; (916) 555-0148</span>
  </div>
</section>

<section class="about-section">
  <div class="about abs" role="img" aria-label="Sacramento skyline and river under a navy overlay"></div>
  <div class="portrait abs" role="img" aria-label="Portrait of the attorney in a dark suit"></div>
  <div class="eyebrow abs">DORIAN KESSEL</div>
  <h2 class="abs" style="left:162px;top:1676px;color:#fff;font-size:34px;font-weight:500">Ready, Reliable, and Experienced</h2>
  <div class="rule about-rule abs"></div>
  <div class="about-copy abs">
    <p>Lorem ipsum dolor sit amet, consectetuer adipiscing elit, sed diam nonummy nibh euismod tincidunt ut laoreet dolore magna aliquam erat volutpat. Ut wisi enim ad minim veniam, quis nostrud exerci tation ullamcorper suscipit lobortis nisl ut aliquip ex ea commodo consequat.</p>
    <p>Duis autem vel eum iriure dolor in hendrerit in vulputate velit esse molestie consequat, vel illum dolore eu feugiat nulla facilisis at vero eros et accumsan et iusto odio dignissim qui blandit praesent luptatum zzril delenit augue duis dolore te feugait nulla facilisi.</p>
  </div>
  <div class="btn btn-gold about-btn abs">Read More About Dorian</div>
</section>

<section class="contact">
  <div class="contact-band abs"></div>
  <h2 class="section-title abs" style="top:2220px">Contact Us</h2>
  <div class="rule abs" style="left:562px;top:2270px"></div>
  <p class="section-lead abs" style="top:2282px;font-size:13.5px;line-height:25px">Lorem ipsum dolor sit amet, consectetuer adipiscing elit, sed diam nonummy nibh euismod tincidunt ut laoreet dolore magna aliquam<br>erat volutpat. Ut wisi enim ad minim veniam, quis nostrud exerci tation ullamcorper suscipit.</p>

  <div class="contact-card abs">
    <form class="form-panel">
      <h3>Schedule A Free Consultation</h3>
      <div class="rule"></div>
      <div class="field"><svg class="icon" viewBox="0 0 20 20"><circle cx="10" cy="6" r="3.5"/><path d="M3 18c0-4 3-6 7-6s7 2 7 6z"/></svg>Name</div>
      <div class="field"><svg class="icon" viewBox="0 0 20 20"><rect x="2" y="4" width="16" height="12"/><path d="M2 4l8 7 8-7"/></svg>Email</div>
      <div class="field"><svg class="icon" viewBox="0 0 20 20"><path d="M4 3l3 0 2 4-2 1.5a10 10 0 0 0 4.5 4.5L13 11l4 2v3a2 2 0 0 1-2 2A13 13 0 0 1 2 5a2 2 0 0 1 2-2z"/></svg>Phone</div>
      <div class="field tall"><svg class="icon" viewBox="0 0 20 20"><path d="M3 4h14v9H8l-4 3v-3H3z"/></svg>Please enter a brief description of your case</div>
      <div class="submit">Submit Now</div>
    </form>
    <div class="info-panel">
      <h3>When You Contact<br>Dorian Kessel Law<br>For A Free Consultation .....</h3>
      <p>Lorem ipsum dolor sit amet, consectetuer adipiscing elit, sed diam nonummy nibh euismod tincidunt ut laoreet dolore magna aliquam erat volutpat.</p>
    </div>
  </div>
</section>

<footer>
  <div class="footer-brand abs"><span class="mark"></span>Dorian Kessel Law</div>
  <div class="social abs"><span></span><span></span><span></span><span></span></div>

  <div class="f-title abs" style="left:550px;top:2885px">Contact Details</div>
  <div class="f-rule abs" style="left:550px;top:2920px;height:2px"></div>
  <div class="f-item abs" style="left:550px;top:2945px">
    <span class="circ"><svg class="icon" viewBox="0 0 20 20"><path d="M10 18s6-6 6-10a6 6 0 0 0-12 0c0 4 6 10 6 10z"/><circle cx="10" cy="8" r="2"/></svg></span>
    <span>2870 Larkspur Avenue<br>Suite #304<br>Elk Grove, CA 95758</span>
  </div>
  <div class="f-item abs" style="left:550px;top:3033px">
    <span class="circ"><svg class="icon" viewBox="0 0 20 20"><path d="M4 3l3 0 2 4-2 1.5a10 10 0 0 0 4.5 4.5L13 11l4 2v3a2 2 0 0 1-2 2A13 13 0 0 1 2 5a2 2 0 0 1 2-2z"/></svg></span>
    <span>Free Consultation<br>(916) 555-0148</span>
  </div>

  <div class="f-title abs" style="left:887px;top:2885px">Quick Links</div>
  <div class="f-rule abs" style="left:887px;top:2920px;height:2px"></div>
  <ul class="quick abs">
    <li>Home</li><li>Dorian Kessel</li><li>Practice Areas</li><li>Insights</li><li>Contact</li><li>Privacy Policy</li>
  </ul>

  <p class="disclaimer abs">The information on this website is for general information purposes only. Nothing on this site should be taken as legal advice for any individual case or situation. This information is not intended to create, and receipt of viewing does not constitute an attorney-client relationship.</p>
  <div class="footer-line abs"></div>
  <p class="copyright abs">© 2021 Dorian Kessel Law. &nbsp;All Rights Reserved.</p>
</footer>

</body>
</html>
```